Restaurant, Nightclub

It's a Restaurant come nightclub. Our sign Lumen is white letters with blue edging on a black back ground.

Industry/Entity Type

Restaurant

Contact Information for Business Card

Lumen Ashbridge & Co
42 Mill Lane
Ashbridge Kent SG2 7PQ

```html
<!DOCTYPE html>
<html lang="en">
<head>
<meta charset="utf-8">
<title>Lumen Ashbridge &amp; Co – Business Card</title>
<link rel="stylesheet" href="https://fonts.googleapis.com/css2?family=Arimo:wght@400&display=swap">
<style>
  :root {
    --page-bg: #d9d9d9;
    --card-black: #0c0c0c;
    --card-sheen: #1c1c1c;
    --ink-white: #ffffff;
    --crease-dark: rgba(0, 0, 0, 0.9);
    --crease-light: rgba(255, 255, 255, 0.08);
  }

  * { box-sizing: border-box; margin: 0; padding: 0; }

  html, body {
    width: 1200px;
    height: 900px;
    overflow: hidden;
  }

  body {
    background: var(--page-bg);
    display: flex;
    align-items: center;
    justify-content: center;
    font-family: "Arimo", Arial, sans-serif;
  }

  .business-card {
    position: relative;
    width: 840px;
    height: 480px;
    background: radial-gradient(ellipse at 45% 40%, var(--card-sheen) 0%, var(--card-black) 70%);
    color: var(--ink-white);
    overflow: hidden;
  }

  .card-crease {
    position: absolute;
    inset: 0;
    width: 100%;
    height: 100%;
  }

  .brand {
    position: absolute;
    left: 60px;
    top: 150px;
    width: 340px;
  }

  .brand-row {
    display: flex;
    align-items: center;
    gap: 16px;
  }

  .brand-mark {
    width: 22px;
    height: 22px;
    background: var(--ink-white);
    flex: none;
  }

  .brand-name {
    font-size: 84px;
    font-weight: 400;
    line-height: 1;
  }

  .brand-tagline {
    display: block;
    margin-top: 10px;
    padding-left: 38px;
    font-size: 19px;
    letter-spacing: 2px;
  }

  .address {
    position: absolute;
    left: 462px;
    top: 132px;
    font-style: normal;
    font-size: 25px;
    line-height: 1.12;
    letter-spacing: 0.5px;
  }
</style>
</head>
<body>
  <article class="business-card">
    <svg class="card-crease" viewBox="0 0 840 480" aria-hidden="true">
      <line x1="412" y1="110" x2="440" y2="300" stroke="var(--crease-dark)" stroke-width="3"/>
      <line x1="414" y1="110" x2="442" y2="300" stroke="var(--crease-light)" stroke-width="1"/>
    </svg>

    <div class="brand">
      <div class="brand-row">
        <span class="brand-mark"></span>
        <span class="brand-name">Lumen</span>
      </div>
      <span class="brand-tagline">Ashbridge &amp; Co</span>
    </div>

    <address class="address">
      42 Mill Lane<br>
      Ashbridge Kent<br>
      SG2 7PQ
    </address>
  </article>
</body>
</html>
```